Web page design for podiatry office*

Need a web page for our podiatry office. It should feature most of our services, hours, directions and location. Should include a short bio of the doctor and a contact page.

Coding

Coded - Design and coding required

Number of Pages Required

1 page

Colors

Designer to choose colors to be used in the design.

```html
<!DOCTYPE html>
<html lang="en">
<head>
<meta charset="utf-8">
<title>Halvorsen Podiatry</title>
<link rel="stylesheet" href="https://fonts.googleapis.com/css2?family=Lato:wght@400;700&family=Montserrat:wght@300;400;500;600;700&display=swap">
<style>
:root{
  --green-dark:#1d6b30;
  --green:#2e8a40;
  --green-light:#7fc275;
  --green-pale:#a9d8a0;
  --text:#222;
  --muted:#555;
  --footer:#2b3a38;
  --white:#fff;
}
*{box-sizing:border-box;margin:0;padding:0}
html,body{width:1200px;height:4136px;overflow:hidden}
body{position:relative;font-family:Lato,sans-serif;color:var(--text);background:var(--white)}
.abs{position:absolute}
.topbar{left:0;top:0;width:1200px;height:40px;background:var(--green-dark);color:#fff;font-size:14px}
.topbar .mail{left:100px;top:11px}
.topbar .portal{left:945px;top:12px;font-size:13px}
.topbar .lang{left:1070px;top:12px;font-size:12px}
.topbar .sep{top:0;width:1px;height:40px;background:rgba(255,255,255,.3)}
.header{left:0;top:40px;width:1200px;height:177px;border-bottom:1px solid #ddd}
.call{left:90px;top:34px}
.call .ring{width:40px;height:40px;border:3px solid var(--green-dark);border-radius:50%;display:flex;align-items:center;justify-content:center}
.call .lbl{left:50px;top:2px;font-size:14px;color:var(--green-dark);white-space:nowrap}
.call .num{left:50px;top:22px;font-size:17px;font-weight:700;white-space:nowrap}
.brand{font-family:Montserrat,sans-serif;font-weight:600;font-size:34px;color:var(--green);white-space:nowrap}
.brand-circle{border:6px solid var(--green-light);border-radius:50%}
.social{display:flex;gap:10px}
.social span{width:40px;height:40px;border-radius:50%;background:var(--green-dark);display:block}
.nav{top:134px;font-size:19px;color:#333}
.nav.active{color:var(--green);font-weight:700}
.hero{left:0;top:217px;width:1200px;height:620px;background:linear-gradient(100deg,#f1ece8 0%,#e6ddd6 40%,#d9cfca 70%,#c8c3c2 100%)}
.hero h1{left:82px;top:170px;font-family:Montserrat,sans-serif;font-size:56px;font-weight:600;color:var(--green-dark)}
.hero p{left:88px;top:248px;width:520px;font-size:16px;font-weight:700;line-height:30px}
.btn{display:inline-flex;align-items:center;gap:8px;border-radius:25px;color:#fff;font-family:Montserrat,sans-serif;font-weight:600;font-size:16px;padding:0 26px;height:48px}
.btn.dark{background:var(--green-dark)}
.btn.light{background:var(--green-light)}
.h2{font-family:Montserrat,sans-serif;font-size:38px;font-weight:300;color:#222;text-align:center}
.h2 b{font-weight:700;color:var(--green-dark)}
.para{font-size:15px;line-height:36px;color:#333}
.divider{left:90px;width:1020px;height:1px;background:#e3e3e3}
.services{left:0;top:1839px;width:1200px;height:700px;background:linear-gradient(90deg,#6fb676,#4f9a62 60%,#3f8a55)}
.card{top:300px;height:193px}
.card .cap{position:absolute;left:0;bottom:0;width:100%;height:34px;background:linear-gradient(90deg,#2e8a40,#7fc275);color:#fff;font-family:Montserrat,sans-serif;font-size:15px;font-weight:600;display:flex;align-items:center;justify-content:center}
.dots{display:flex;gap:16px}
.dots i{width:15px;height:15px;border:2px solid #333;border-radius:50%;display:block}
.dots i.on{box-shadow:inset 0 0 0 3px #fff,inset 0 0 0 8px #333}
.dots.white i{border-color:#fff}
.dots.white i.on{box-shadow:inset 0 0 0 3px transparent,inset 0 0 0 8px #fff}
.blog-img{top:2679px;width:328px;height:196px}
.date{position:absolute;left:14px;bottom:-2px;background:var(--green-light);color:#fff;font-size:13px;padding:5px 12px}
.blog-title{top:2915px;font-family:Montserrat,sans-serif;font-size:19px;color:var(--green);font-weight:500}
.blog-text{top:2950px;width:320px;font-size:12px;line-height:25px;color:#333}
.blog-more{top:3028px;font-size:16px;color:var(--green)}
.footer{left:0;top:3573px;width:1200px;height:563px;background:linear-gradient(160deg,#2f3d3f,#263433 60%,#1f2c36)}
.f-icon{width:84px;height:84px;border-radius:50%;background:var(--green);display:flex;align-items:center;justify-content:center}
.f-text{color:#fff;font-size:17px;line-height:28px;text-align:center}
</style>
</head>
<body>

<div class="abs topbar">
  <div class="abs mail">✉ info@halvorsenfootcare.com</div>
  <div class="abs sep" style="left:326px"></div>
  <div class="abs sep" style="left:928px"></div>
  <div class="abs portal">Patient Portal</div>
  <div class="abs sep" style="left:1057px"></div>
  <div class="abs lang">EN ▾</div>
  <div class="abs sep" style="left:1110px"></div>
</div>

<header class="abs header">
  <div class="abs call">
    <div class="ring"><svg width="20" height="20" viewBox="0 0 24 24"><path d="M6.6 10.8a15 15 0 0 0 6.6 6.6l2.2-2.2c.3-.3.7-.4 1-.2 1.1.4 2.3.6 3.6.6.6 0 1 .4 1 1V20c0 .6-.4 1-1 1C10.6 21 3 13.4 3 4c0-.6.4-1 1-1h3.5c.6 0 1 .4 1 1 0 1.3.2 2.5.6 3.6.1.3 0 .7-.2 1z" fill="#1d6b30"/></svg></div>
    <div class="abs lbl">Call us:</div>
    <div class="abs num">+1-555-010-0199</div>
  </div>
  <div class="abs brand" style="left:318px;top:66px">Halvorsen</div>
  <div class="abs brand-circle" style="left:518px;top:8px;width:166px;height:166px"></div>
  <div class="abs brand" style="left:705px;top:62px">Podiatry</div>
  <div class="abs social" style="left:919px;top:36px"><span></span><span></span><span></span><span></span></div>
  <div class="abs nav active" style="left:133px">Home</div>
  <div class="abs nav" style="left:234px">About Us</div>
  <div class="abs nav" style="left:364px">Our Services</div>
  <div class="abs nav" style="left:718px">Cases &amp; Reviews</div>
  <div class="abs nav" style="left:916px">Blog</div>
  <div class="abs nav" style="left:1004px">Contact</div>
</header>

<section class="abs hero" role="img" aria-label="Podiatrist in a mask treating a patient's foot">
  <h1 class="abs">The Stride Clinic</h1>
  <p class="abs">Lorem ipsum dolor sit amet, consectetur adipiscing elit, sed do eiusmod tempor incididunt aliqua.</p>
  <div class="abs btn light" style="left:88px;top:328px;background:var(--green)">➤ Helpful Tips</div>
  <svg class="abs" style="left:0;top:540px" width="1200" height="82" viewBox="0 0 1200 82" preserveAspectRatio="none">
    <path d="M0 52 C300 -10 600 60 900 55 C1050 52 1150 40 1200 30 L1200 82 L0 82Z" fill="#fff"/>
    <path d="M0 52 C300 -8 560 40 760 48" stroke="#1d6b30" stroke-width="6" fill="none"/>
  </svg>
</section>

<h2 class="abs h2" style="left:0;top:910px;width:1200px">Welcome to <b>Halvorsen Podiatry</b></h2>
<p class="abs para" style="left:110px;top:975px;width:980px;text-align:center">Sed ut perspiciatis unde omnis iste natus error sit voluptatem accusantium doloremque laudantium, totam rem aperiam, eaque ipsa quae ab illo inventore veritatis et quasi architecto beatae vitae dicta sunt explicabo. Nemo enim ipsam aspernatur aut odit aut fugit, sed quia consequuntur magni dolores eos qui ratione voluptatem sequi nesciunt.</p>
<div class="abs btn dark" style="left:380px;top:1104px">Read More ➜</div>
<div class="abs btn light" style="left:574px;top:1104px">Get An Appointment ➜</div>

<div class="abs divider" style="top:1230px"></div>

<svg class="abs" style="left:50px;top:1305px" width="470" height="460" viewBox="0 0 470 460">
  <circle cx="231" cy="229" r="222" fill="none" stroke="#7fc275" stroke-width="14"/>
</svg>
<div class="abs" role="img" aria-label="Podiatrist examining a patient's foot under a lamp" style="left:85px;top:1345px;width:390px;height:390px;border-radius:50%;background:radial-gradient(circle at 40% 40%,#e9e4e0,#b9bcc0 70%,#8f9ea8)"></div>
<h2 class="abs h2" style="left:548px;top:1378px;text-align:left">About <b>Halvorsen Podiatry</b></h2>
<p class="abs para" style="left:548px;top:1432px;width:562px;text-align:justify">Sed ut perspiciatis unde omnis iste natus error sit voluptatem accusantium doloremque laudantium, totam rem aperiam, eaque ipsa quae ab illo inventore veritatis et quasi architecto beatae vitae dicta sunt explicabo. Nemo enim ipsam voluptatem quia voluptas sit aspernatur aut odit aut fugit, sed eos qui ratione voluptatem sequi nesciunt.</p>
<div class="abs btn" style="left:548px;top:1629px;background:var(--green)">View More Bio ➜</div>

<section class="abs services" role="img" aria-label="Faded green-tinted clinic background">
  <svg class="abs" style="left:0;top:-4px" width="1200" height="80" viewBox="0 0 1200 80" preserveAspectRatio="none">
    <path d="M0 0 H1200 V0 C1000 10 850 30 700 55 C500 85 200 40 0 30Z" fill="#fff"/>
    <path d="M700 55 C850 25 1050 10 1200 5" stroke="#1d6b30" stroke-width="8" fill="none"/>
  </svg>
  <h2 class="abs h2" style="left:0;top:134px;width:1200px;color:#fff"><span style="font-weight:300">Our</span> <b style="color:#fff">Services</b></h2>
  <p class="abs para" style="left:130px;top:203px;width:940px;text-align:center;color:#fff;font-size:15px">Sed ut perspiciatis unde omnis iste natus error sit voluptatem accusantium doloremque laudantium, totam rem aperiam, eaque ipsa quae ab illo inventore veritatis et quasi architecto beatae vitae dicta sunt explicabo.</p>
  <div class="abs card" style="left:98px;width:323px;background:linear-gradient(135deg,#eef0f2,#d9c6bb)" role="img" aria-label="Foot treatment with instrument"><div class="cap">Custom Orthotics</div></div>
  <div class="abs card" style="left:438px;width:320px;background:#2f7d45">
    <div class="abs" style="left:22px;top:16px;width:276px;height:161px;border:2px dashed rgba(255,255,255,.6);display:flex;flex-direction:column;align-items:center;justify-content:center;color:#fff">
      <div style="font-family:Montserrat,sans-serif;font-size:23px;font-weight:600">Diabetic Foot Care</div>
      <div style="font-size:15px;margin-top:6px">Read More ➜</div>
    </div>
  </div>
  <div class="abs card" style="left:779px;width:323px;background:linear-gradient(135deg,#eef0f4,#9fb3e8 60%,#e4ccbf)" role="img" aria-label="Gloved hands examining a foot"><div class="cap">Diagnostic Testing</div></div>
  <div class="abs dots white" style="left:562px;top:531px"><i></i><i class="on"></i><i></i></div>
  <svg class="abs" style="left:0;top:620px" width="1200" height="82" viewBox="0 0 1200 82" preserveAspectRatio="none">
    <path d="M0 80 C250 70 550 40 750 20 C950 0 1100 10 1200 20 V82 H0Z" fill="#fff"/>
    <path d="M0 75 C250 65 520 35 720 22" stroke="#1d6b30" stroke-width="10" fill="none"/>
  </svg>
</section>

<h2 class="abs h2" style="left:0;top:2603px;width:1200px;font-size:34px">Our <b>Blog</b></h2>
<div class="abs blog-img" style="left:90px;background:linear-gradient(135deg,#e8e2dc,#d8b8a0)" role="img" aria-label="Foot being examined with a pen"><span class="date">📅 Oct 27 2019</span></div>
<div class="abs blog-img" style="left:435px;background:linear-gradient(135deg,#c9d8e2,#eceae6)" role="img" aria-label="Podiatrist using a drill on a foot"><span class="date">📅 Jul 27 2019</span></div>
<div class="abs blog-img" style="left:782px;background:linear-gradient(135deg,#eef0f4,#5d6470 60%,#d9b4a0)" role="img" aria-label="Gloved hands treating a toenail"><span class="date">📅 Jul 02 2019</span></div>
<div class="abs blog-title" style="left:90px">Sed ut perspiciatis und</div>
<div class="abs blog-title" style="left:435px">Sed ut perspiciatis und</div>
<div class="abs blog-title" style="left:782px">Sed ut perspiciatis und</div>
<p class="abs blog-text" style="left:90px">Sed ut perspiciatis unde omnis iste natus error sit voluptatem accusantium doloremque laudantium, totam rem aperiam, eaque ipsa quae ab illo</p>
<p class="abs blog-text" style="left:435px">Sed ut perspiciatis unde omnis iste natus error sit voluptatem accusantium doloremque laudantium, totam rem aperiam, eaque ipsa quae ab illo</p>
<p class="abs blog-text" style="left:782px">Sed ut perspiciatis unde omnis iste natus error sit voluptatem accusantium doloremque laudantium, totam rem aperiam, eaque ipsa quae ab illo</p>
<div class="abs blog-more" style="left:90px">Read More</div>
<div class="abs blog-more" style="left:435px">Read More</div>
<div class="abs blog-more" style="left:782px">Read More</div>

<div class="abs divider" style="top:3120px"></div>

<h2 class="abs h2" style="left:0;top:3188px;width:1200px;font-size:36px">Cases &amp; <b>Reviews</b></h2>
<div class="abs" style="left:0;top:3238px;width:1200px;text-align:center;font-family:Georgia,serif;font-size:90px;line-height:80px;color:var(--green-pale);font-weight:700">“</div>
<div class="abs" style="left:0;top:3314px;width:1200px;text-align:center;font-size:24px;color:#f2a500;letter-spacing:2px">★★★★★</div>
<p class="abs para" style="left:180px;top:3347px;width:840px;text-align:center;color:var(--muted);font-family:Montserrat,sans-serif;font-size:15px">Sed ut perspiciatis unde omnis iste natus error sit voluptatem accusantium doloremque laudantium, totam rem aperiam, eaque ipsa quae ab illo inventore explicabo.</p>
<div class="abs" style="left:0;top:3421px;width:1200px;text-align:center;font-family:Montserrat,sans-serif;font-size:27px;font-weight:600;color:var(--green-dark)">Mara Quill</div>
<div class="abs dots" style="left:562px;top:3470px"><i></i><i class="on"></i><i></i></div>

<footer class="abs footer">
  <svg class="abs" style="left:0;top:-8px" width="1200" height="90" viewBox="0 0 1200 90" preserveAspectRatio="none">
    <path d="M0 0 H1200 V20 C1050 60 800 60 650 45 C500 25 300 0 0 30Z" fill="#fff"/>
    <path d="M390 8 C520 20 620 45 760 48 C950 50 1100 35 1200 10" stroke="#1d6b30" stroke-width="8" fill="none"/>
  </svg>
  <div class="abs brand" style="left:330px;top:142px;color:var(--green)">Halvorsen</div>
  <div class="abs brand-circle" style="left:535px;top:110px;width:114px;height:114px;border-color:var(--green)"></div>
  <div class="abs brand" style="left:670px;top:142px;color:var(--green)">Podiatry</div>

  <div class="abs f-icon" style="left:257px;top:255px"><svg width="40" height="46" viewBox="0 0 24 28"><path d="M12 2a8 8 0 0 0-8 8c0 6 8 14 8 14s8-8 8-14a8 8 0 0 0-8-8z" fill="none" stroke="#fff" stroke-width="1.6"/><circle cx="12" cy="10" r="3" fill="none" stroke="#fff" stroke-width="1.6"/><ellipse cx="12" cy="25" rx="7" ry="2" fill="none" stroke="#fff" stroke-width="1.2"/></svg></div>
  <div class="abs f-icon" style="left:553px;top:255px"><svg width="40" height="40" viewBox="0 0 24 24"><path d="M6.6 10.8a15 15 0 0 0 6.6 6.6l2.2-2.2c.3-.3.7-.4 1-.2 1.1.4 2.3.6 3.6.6.6 0 1 .4 1 1V20c0 .6-.4 1-1 1C10.6 21 3 13.4 3 4c0-.6.4-1 1-1h3.5c.6 0 1 .4 1 1 0 1.3.2 2.5.6 3.6.1.3 0 .7-.2 1z" fill="none" stroke="#fff" stroke-width="1.5"/></svg></div>
  <div class="abs f-icon" style="left:864px;top:255px"><svg width="34" height="40" viewBox="0 0 20 24"><path d="M3 2h14M3 22h14M5 2c0 6 10 6 10 10S5 16 5 22M15 2c0 6-10 6-10 10s10 4 10 10" fill="none" stroke="#fff" stroke-width="1.6"/></svg></div>

  <div class="abs f-text" style="left:150px;top:348px;width:300px">77 Linden Row, Suite 12<br>Ashford, MA 01000</div>
  <div class="abs f-text" style="left:446px;top:348px;width:300px">Phone:<br>1-555-010-0199</div>
  <div class="abs f-text" style="left:757px;top:348px;width:300px">Opening Hours<br>Mon - Fri: 10:00 am - 06:00 pm</div>

  <div class="abs" style="left:0;top:426px;width:1200px;text-align:center;color:#fff;font-size:15px">Home &nbsp;|&nbsp; About Us &nbsp;|&nbsp; Services &nbsp;|&nbsp; Cases &amp; Reviews &nbsp;|&nbsp; Blog &nbsp;|&nbsp; Contact</div>
  <div class="abs" style="left:0;top:467px;width:1200px;text-align:center;color:#fff;font-size:14px">© 2019 Company Name. All right reserved</div>
  <div class="abs" style="left:533px;top:506px;display:flex;gap:6px">
    <span style="width:30px;height:30px;border:2px solid #fff;border-radius:50%;display:block"></span>
    <span style="width:30px;height:30px;border:2px solid #fff;border-radius:50%;display:block"></span>
    <span style="width:30px;height:30px;border:2px solid #fff;border-radius:50%;display:block"></span>
    <span style="width:30px;height:30px;border:2px solid #fff;border-radius:50%;display:block"></span>
  </div>
</footer>

</body>
</html>
```